Business card

We need a business card design for our company based in Auckland , New Zealand called 'Kestrel + Design Ltd'. We provide architectural services. We would like to see designs that use the max. three colours (such as white, black, grey) The final design should communicate financial safety and growth."
Also I will provide our company logo. I would like to the logo to be embeded onto our business card.

Target Market(s)

new residential house, alteration & addition & light commericila design & drafting service

Industry/Entity Type

Architecture

Contact Information for Business Card

Company name: kestrel + design Ltd.
Name: Mark Telford
Job title: architectural designer & Design RQC
email address: mark@kdstudio.co.nz
mobile number: 02 5319 6620
web site: www.kdstudio.co.nz

Requirements
Must have
• My project must have..
• - embeded logo (attached company logo)
• I don't have a bigger version for our company logo, but I have one old one, so you can remove the word from it)
• - insert the attached small PDGQ logo & RQC logo
• - creative, simple and clear business card.
• - Max. three colours
Nice to have
• - Here are the samples I would like to share with you: http://www.velmorindex.com/blog/minimalistic-business-card-designs/
• I would like to have my business card like one of the creation.
Should not have
• TBA

```html
<!DOCTYPE html>
<html lang="en">
<head>
<meta charset="utf-8">
<title>Kestrel + Design Ltd — Business Card</title>
<link rel="stylesheet" href="https://fonts.googleapis.com/css2?family=Open+Sans:wght@400;600;700&display=swap">
<style>
  :root {
    --ink: #0d0d0d;
    --paper: #ffffff;
    --paper-shade: #e4e4e4;
    --mid-grey: #6f6f6f;
    --soft-grey: #9a9a9a;
    --backdrop: #d9d9d9;
  }
  * { box-sizing: border-box; margin: 0; padding: 0; }
  html, body {
    width: 1200px; height: 950px; overflow: hidden;
    background: var(--backdrop);
    font-family: "Open Sans", sans-serif;
  }
  .card {
    position: absolute; left: 232px; width: 735px; height: 420px;
    overflow: hidden;
    box-shadow: 0 6px 18px rgba(0,0,0,0.18);
  }
  .card--back { top: 40px; background: linear-gradient(160deg, var(--paper) 0%, var(--paper-shade) 100%); }
  .card--front { top: 490px; background: var(--paper); }
  .card__art { position: absolute; inset: 0; width: 100%; height: 100%; }

  /* back */
  .affiliations {
    position: absolute; left: 0; right: 0; top: 130px;
    display: flex; align-items: center; justify-content: center; gap: 40px;
  }
  .affiliation__name {
    display: flex; align-items: center; gap: 12px;
    font-size: 44px; font-weight: 700; color: var(--ink); letter-spacing: 1px;
  }
  .affiliation__mark { width: 16px; height: 16px; background: var(--ink); }
  .affiliations__divider { width: 2px; height: 110px; background: var(--soft-grey); }
  .badge { width: 110px; height: 110px; border-radius: 50%; background: var(--ink); }
  .back__web {
    position: absolute; left: 0; right: 0; top: 300px; text-align: center;
    font-size: 18px; color: var(--mid-grey); letter-spacing: 0.5px;
  }

  /* front */
  .holder { position: absolute; left: 50px; top: 112px; color: var(--paper); }
  .holder__name { font-size: 24px; font-weight: 600; letter-spacing: 1px; text-transform: uppercase; }
  .holder__title { font-size: 17px; line-height: 1.35; margin-top: 8px; width: 240px; }
  .contacts { list-style: none; margin-top: 26px; font-size: 17px; line-height: 1.45; }
  .contacts li { display: flex; align-items: center; gap: 10px; }
  .contacts svg { width: 14px; height: 14px; fill: var(--paper); flex: none; }
  .company-mark {
    position: absolute; left: 450px; top: 150px;
    display: flex; align-items: center; gap: 12px;
    font-size: 28px; font-weight: 600; color: var(--ink);
  }
  .company-mark__square { width: 14px; height: 14px; background: var(--ink); }
  .company-name {
    position: absolute; right: 40px; bottom: 22px;
    font-size: 22px; font-weight: 700; color: var(--paper);
  }
</style>
</head>
<body>

<section class="card card--back" aria-label="Card reverse">
  <div class="affiliations">
    <div class="affiliation__name"><span class="affiliation__mark"></span>PDGQ</div>
    <span class="affiliations__divider"></span>
    <div class="badge" role="img" aria-label="Practitioner certification badge"></div>
  </div>
  <p class="back__web">www.kdstudio.co.nz</p>
</section>

<section class="card card--front" aria-label="Card front">
  <svg class="card__art" viewBox="0 0 735 420" preserveAspectRatio="none" aria-hidden="true">
    <path fill="var(--mid-grey)" d="M0,52 C90,10 200,0 285,12 L285,26 C200,18 110,30 0,78 Z"/>
    <path fill="var(--ink)" d="M0,82 C90,40 180,28 250,36 C310,120 300,230 390,292 C480,350 620,345 735,332 L735,420 L0,420 Z"/>
    <path fill="var(--soft-grey)" d="M420,296 C520,336 640,326 735,300 L735,318 C630,346 520,340 420,296 Z"/>
  </svg>

  <div class="holder">
    <h1 class="holder__name">Mark Telford</h1>
    <p class="holder__title">architectural designer &amp; Design RQC</p>
    <ul class="contacts">
      <li><svg viewBox="0 0 14 14"><rect x="3" y="0" width="8" height="14" rx="1.5"/><rect x="5" y="2" width="4" height="8" fill="#0d0d0d"/></svg>02 5319 6620</li>
      <li><svg viewBox="0 0 14 14"><rect x="0" y="2" width="14" height="10" rx="1"/><path d="M0,3 L7,8 L14,3" stroke="#0d0d0d" stroke-width="1.4" fill="none"/></svg>mark@kdstudio.co.nz</li>
      <li><svg viewBox="0 0 14 14"><circle cx="7" cy="7" r="7"/><path d="M0,7 H14 M7,0 V14" stroke="#0d0d0d" stroke-width="1.2"/></svg>www.kdstudio.co.nz</li>
    </ul>
  </div>

  <div class="company-mark"><span class="company-mark__square"></span>Kestrel + Design</div>
  <p class="company-name">kestrel + design Ltd.</p>
</section>

</body>
</html>
```